Intelligent design image for our website

I would like an awesome image for our website that showcases the intelligent design of our app. We currently have a test web site here.
https://www.roadpine.com.au/test-ewd/
I really do not like the graphic next to the "Intelligent design" and i want something much better than this.
Our app is used by Australian Truck Drivers. It would be nice to have a little bit of an Australian feel, but most importantly is should clearly showcase our app look a feel and the screens should be as legible (readable) as possible. These examples could be used for inspiration.
https://pixelmarigold.net/products/free-app-showcase-mockup-psd-3903046
https://www.vantrel.com/community/file/1118736476036244148/MobileApp-Landing-Page-Template-for-Mobile-Apps-Showcase

```html
<!DOCTYPE html>
<html lang="en">
<head>
<meta charset="utf-8">
<title>Work Diary App – Compliance Screen</title>
<link href="https://fonts.googleapis.com/css2?family=Lato:wght@400;700;900&display=swap" rel="stylesheet">
<style>
  :root{
    --page-bg:#eceef1;
    --screen-bg:#f3f4f6;
    --card-bg:#ffffff;
    --ink:#1f2328;
    --muted:#6b7280;
    --line:#e3e6ea;
    --brand:#2b9fe0;
    --brand-dark:#1d6fd6;
    --bar-track:#9fc4f0;
    --ok:#35b35a;
  }
  *{box-sizing:border-box;margin:0;padding:0}
  html,body{width:1200px;height:1200px;overflow:hidden}
  body{background:var(--page-bg);font-family:"Lato",sans-serif;color:var(--ink);position:relative}

  .app-screen{
    position:absolute;left:320px;top:30px;width:560px;height:1140px;
    background:var(--screen-bg);border-radius:44px;overflow:hidden;
    box-shadow:0 20px 50px rgba(0,0,0,.12);
    display:flex;flex-direction:column;
  }
  .status-bar{height:50px;background:var(--card-bg);display:flex;align-items:center;justify-content:space-between;padding:0 36px;font-weight:700;font-size:19px}
  .status-icons{display:flex;gap:8px;align-items:center}

  .app-header{background:var(--card-bg);height:78px;display:flex;align-items:center;padding:0 24px;gap:18px;border-bottom:1px solid var(--line)}
  .driver{flex:1}
  .driver-name{font-weight:900;font-size:20px}
  .driver-licence{font-size:16px;color:var(--muted);margin-top:4px}
  .sync{display:flex;flex-direction:column;align-items:flex-end;gap:4px}
  .sync-btn{background:var(--brand);color:#fff;font-size:14px;font-weight:700;padding:5px 10px;border-radius:4px}

  .content{flex:1;padding:0 14px;display:flex;flex-direction:column;gap:14px;overflow:hidden}

  .card{background:var(--card-bg);border-radius:10px;box-shadow:0 2px 6px rgba(0,0,0,.08);position:relative}
  .card-partial{border-radius:0 0 10px 10px;padding:6px 20px 14px}
  .card-tab{
    display:block;margin:0 auto;width:260px;height:34px;background:var(--brand);color:#fff;
    font-weight:700;font-size:17px;text-align:center;line-height:34px;
    clip-path:polygon(0 0,100% 0,92% 100%,8% 100%);
  }
  .card-rule{border-top:3px solid var(--brand)}
  .card-tab.wide{width:330px}
  .info-icon{position:absolute;right:14px;top:8px}

  .stat-row{display:grid;grid-template-columns:1fr 1fr;text-align:center}
  .stat-row + .stat-row{border-top:1px solid var(--line)}
  .stat{padding:12px 6px}
  .stat + .stat{border-left:1px solid var(--line)}
  .stat-value{font-weight:900;font-size:20px}
  .stat-label{font-size:14px;color:var(--muted);margin-top:3px}

  .period{display:grid;grid-template-columns:1fr 1fr;text-align:center;padding:14px 0 10px;border-bottom:2px solid var(--brand)}

  .progress{padding:14px 20px 10px}
  .progress-title{font-size:14px;color:var(--muted);margin-bottom:6px}
  .bar{height:12px;border-radius:6px;background:var(--bar-track);overflow:hidden}
  .bar-fill{height:100%;background:var(--brand-dark);border-radius:6px 0 0 6px}
  .bar-scale{display:flex;justify-content:space-between;font-size:13px;color:var(--muted);margin-top:6px}

  .pager{display:flex;align-items:center;justify-content:space-between;padding:10px 20px 16px}
  .pager-btn{border:1.5px solid var(--brand);color:var(--brand);font-size:14px;border-radius:4px;padding:6px 16px;width:116px;text-align:center}
  .pager-count{text-align:center}
  .pager-count b{font-size:17px;font-weight:900}
  .pager-count span{display:block;font-size:13px;color:var(--muted)}

  .tab-bar{height:104px;background:var(--card-bg);border-top:1px solid var(--line);display:grid;grid-template-columns:repeat(4,1fr);align-items:center;text-align:center;padding-bottom:16px}
  .tab-item{font-size:14px;font-weight:700;display:flex;flex-direction:column;align-items:center;gap:6px}
</style>
</head>
<body>
  <main class="app-screen">
    <div class="status-bar">
      <span>8:48</span>
      <span class="status-icons">
        <svg width="22" height="14" viewBox="0 0 22 14"><rect x="0" y="9" width="4" height="5" fill="#1f2328"/><rect x="6" y="6" width="4" height="8" fill="#1f2328"/><rect x="12" y="3" width="4" height="11" fill="#1f2328"/><rect x="18" y="0" width="4" height="14" fill="#1f2328"/></svg>
        <svg width="28" height="14" viewBox="0 0 28 14"><rect x="0.5" y="0.5" width="24" height="13" rx="3" fill="none" stroke="#1f2328"/><rect x="3" y="3" width="15" height="8" rx="1" fill="#1f2328"/><rect x="25.5" y="4.5" width="2" height="5" fill="#1f2328"/></svg>
      </span>
    </div>

    <header class="app-header">
      <svg width="22" height="16" viewBox="0 0 22 16"><path d="M0 1h22M0 8h16M0 15h22" stroke="#1f2328" stroke-width="2.4"/></svg>
      <div class="driver">
        <div class="driver-name">John Smith</div>
        <div class="driver-licence">License : 1234567890</div>
      </div>
      <div class="sync">
        <svg width="18" height="18" viewBox="0 0 18 18"><circle cx="9" cy="9" r="8" fill="var(--ok)"/><path d="M5 9.5l3 3 5-6" stroke="#fff" stroke-width="2" fill="none"/></svg>
        <span class="sync-btn">Sync Now</span>
      </div>
    </header>

    <section class="content">
      <div class="card card-partial">
        <div class="stat-row">
          <div class="stat"><div class="stat-value">15:30</div><div class="stat-label">Period Remaining</div></div>
          <div class="stat"><div class="stat-value">0 / 1</div><div class="stat-label">7 hr Rests Found/Required</div></div>
        </div>
        <div class="pager" style="padding:8px 0 0">
          <span class="pager-btn">&lt; Previous</span>
          <span class="pager-count"><b>1/1</b><span>Active Periods</span></span>
          <span class="pager-btn">Next &gt;</span>
        </div>
      </div>

      <div class="card card-rule">
        <span class="card-tab">14 day Rule</span>
        <svg class="info-icon" width="24" height="24" viewBox="0 0 24 24"><circle cx="12" cy="12" r="10.5" fill="none" stroke="var(--brand)" stroke-width="2"/><rect x="11" y="10" width="2" height="8" fill="var(--brand)"/><circle cx="12" cy="7" r="1.4" fill="var(--brand)"/></svg>
        <div class="period">
          <div><div class="stat-value">01:17 14-Aug</div><div class="stat-label">Period Start</div></div>
          <div><div class="stat-value">01:17 28-Aug</div><div class="stat-label">Period End</div></div>
        </div>
        <div class="progress">
          <div class="progress-title">Work Completed</div>
          <div class="bar"><div class="bar-fill" style="width:54%"></div></div>
          <div class="bar-scale"><span>0 hr</span><span>144 hr</span></div>
        </div>
        <div class="stat-row">
          <div class="stat"><div class="stat-value">78:08</div><div class="stat-label">Work Completed</div></div>
          <div class="stat"><div class="stat-value">43:01</div><div class="stat-label">Maximum Continuous Rest</div></div>
        </div>
        <div class="stat-row">
          <div class="stat"><div class="stat-value">65:52</div><div class="stat-label">Work Remaining</div></div>
          <div class="stat"><div class="stat-value">01:17 27-Aug</div><div class="stat-label">Start 24 hr Rest Before</div></div>
        </div>
        <div class="stat-row">
          <div class="stat"><div class="stat-value">62:29</div><div class="stat-label">Period Remaining</div></div>
          <div class="stat"><div class="stat-value">1 / 2</div><div class="stat-label">24 hr Rests Found/Required</div></div>
        </div>
        <div class="pager">
          <span class="pager-btn">&lt; Previous</span>
          <span class="pager-count"><b>1/4</b><span>Active Periods</span></span>
          <span class="pager-btn">Next &gt;</span>
        </div>
      </div>

      <div class="card card-rule">
        <span class="card-tab wide">Total Work Since Last 24 hr Rest</span>
        <svg class="info-icon" width="24" height="24" viewBox="0 0 24 24"><circle cx="12" cy="12" r="10.5" fill="none" stroke="var(--brand)" stroke-width="2"/><rect x="11" y="10" width="2" height="8" fill="var(--brand)"/><circle cx="12" cy="7" r="1.4" fill="var(--brand)"/></svg>
        <div class="progress">
          <div class="bar"><div class="bar-fill" style="width:30%"></div></div>
          <div class="bar-scale"><span>0 hr</span><span>84 hr</span></div>
        </div>
        <div class="stat-row">
          <div class="stat"><div class="stat-value">02:33 23-Aug</div><div class="stat-label">End of 24 hr Rest</div></div>
          <div class="stat"><div class="stat-value">25:03</div><div class="stat-label">Total Work</div></div>
        </div>
      </div>
    </section>

    <nav class="tab-bar">
      <div class="tab-item">
        <svg width="26" height="26" viewBox="0 0 26 26"><path d="M8 6a9 9 0 1 0 10 0" fill="none" stroke="#1f2328" stroke-width="2"/><path d="M13 2v10" stroke="#1f2328" stroke-width="2"/></svg>Logout</div>
      <div class="tab-item">
        <svg width="26" height="26" viewBox="0 0 26 26"><path d="M17 4H5v18h12v-5" fill="none" stroke="#1f2328" stroke-width="2"/><path d="M10 13h12M18 9l4 4-4 4" fill="none" stroke="#1f2328" stroke-width="2"/></svg>Compliance</div>
      <div class="tab-item">
        <svg width="26" height="26" viewBox="0 0 26 26"><rect x="3" y="6" width="20" height="14" fill="none" stroke="#1f2328" stroke-width="2"/><path d="M3 6l10 8 10-8" fill="none" stroke="#1f2328" stroke-width="2"/></svg>Report transfer</div>
      <div class="tab-item">
        <svg width="26" height="26" viewBox="0 0 26 26"><path d="M10 4h12v18H10" fill="none" stroke="#1f2328" stroke-width="2"/><path d="M3 13h12M11 9l4 4-4 4" fill="none" stroke="#1f2328" stroke-width="2"/></svg>Return to Shift</div>
    </nav>
  </main>
</body>
</html>
```